Business Card Design for Contracting

I need a Busines card design for a new Busines (sole trader) based in Sydney, Australia. The business has been set up so I can contract my services to companies. The service I provide is mainly in the civil engineering discipline with the services that can be provided being contract project management, contract estimating, contract time controls and contract financial controls. I would like the design to have the colour blue used.

Target Market(s)

Large to medium Construction companies.

Industry/Entity Type

Construction

Contact Information for Business Card

Pelloway Civil Engineering Services
P.O. Box 418
Brambleford, NSW, 2093

Mobile: 0412 958 231

Email: marcus.pelloway@pcvx.com.au
Web: PCVX.com.au

Font styles to use
Sans Serif

Colors
0493ce
34a6d7
85cae6

Requirements
Must have
• my project must have my name and qualification:
• Marcus Pelloway
• BE (Civil), MTRQAust.

```html
<!DOCTYPE html>
<html lang="en">
<head>
<meta charset="utf-8">
<title>Pelloway Civil Engineering Services – Business Card</title>
<link rel="stylesheet" href="https://fonts.googleapis.com/css2?family=Open+Sans:wght@400;600&family=Roboto+Condensed:wght@700&display=swap">
<style>
  :root {
    --brand-blue: #0493ce;
    --brand-blue-mid: #34a6d7;
    --brand-blue-light: #85cae6;
    --ink-blue: #0b7bb8;
    --ink-grey: #7a7a7a;
    --rule-grey: #a9a9a9;
    --card-white: #ffffff;
    --backdrop: #e9ecef;
  }
  * { box-sizing: border-box; margin: 0; padding: 0; }
  html, body {
    width: 1200px;
    height: 1000px;
    overflow: hidden;
    background: var(--backdrop);
    font-family: "Open Sans", Arial, sans-serif;
  }
  .stage { position: relative; width: 1200px; height: 1000px; }

  .card {
    position: absolute;
    left: 265px;
    width: 665px;
    height: 397px;
    border-radius: 22px;
    overflow: hidden;
    box-shadow: 0 4px 14px rgba(0,0,0,0.18);
  }
  .card-front { top: 73px; background: var(--card-white); }
  .card-back { top: 533px; }

  .wordmark {
    position: absolute;
    left: 0; right: 0;
    text-align: center;
    font-family: "Open Sans", Arial, sans-serif;
    font-weight: 600;
    text-transform: uppercase;
  }
  .card-front .wordmark { top: 70px; color: var(--ink-blue); }
  .card-back .wordmark { top: 130px; color: var(--card-white); }
  .wordmark-mark {
    display: block;
    width: 58px; height: 58px;
    margin: 0 auto 16px;
    background: currentColor;
  }
  .wordmark-name {
    display: block;
    font-size: 23px;
    line-height: 30px;
    letter-spacing: 0.5px;
    white-space: nowrap;
  }
  .wordmark-sub {
    display: flex;
    align-items: center;
    justify-content: center;
    gap: 12px;
    width: 446px;
    margin: 2px auto 0;
    font-size: 14px;
    line-height: 20px;
    letter-spacing: 4px;
  }
  .wordmark-sub::before,
  .wordmark-sub::after {
    content: "";
    flex: 1;
    height: 1px;
    background: currentColor;
  }
  .card-front .wordmark-sub { color: var(--rule-grey); }

  .holder {
    position: absolute;
    top: 256px; left: 0; right: 0;
    text-align: center;
    color: var(--ink-blue);
  }
  .holder-name {
    font-family: "Roboto Condensed", "Arial Narrow", sans-serif;
    font-weight: 700;
    font-size: 22px;
  }
  .holder-quals { font-size: 16px; }

  .contact {
    position: absolute;
    top: 290px; left: 0; right: 0;
    text-align: center;
    color: var(--ink-grey);
  }
  .contact-phone { font-size: 16px; line-height: 22px; }
  .contact-email,
  .contact-web { font-size: 14px; line-height: 20px; }

  .address-band {
    position: absolute;
    left: 0; right: 0; bottom: 0;
    height: 42px;
    background: var(--brand-blue);
    color: var(--card-white);
    font-size: 16px;
    display: flex;
    align-items: center;
    justify-content: center;
    gap: 12px;
  }

  .back-photo {
    position: absolute;
    inset: 0;
    background: linear-gradient(135deg, var(--brand-blue-mid) 0%, var(--brand-blue) 55%, #0489c0 100%);
  }
</style>
</head>
<body>
<main class="stage">
  <section class="card card-front" aria-label="Business card front">
    <div class="wordmark">
      <span class="wordmark-mark" aria-hidden="true"></span>
      <span class="wordmark-name">Pelloway Civil Engineering</span>
      <span class="wordmark-sub">Services</span>
    </div>
    <p class="holder">
      <span class="holder-name">Marcus Pelloway</span>
      <span class="holder-quals">/ BE (Civil), MTRQAust.</span>
    </p>
    <div class="contact">
      <p class="contact-phone">0412 958 231</p>
      <p class="contact-email">marcus.pelloway@pcvx.com.au</p>
      <p class="contact-web">PCVX.com.au</p>
    </div>
    <footer class="address-band">
      <span>P.O. Box 418</span><span>|</span>
      <span>Brambleford</span><span>|</span>
      <span>NSW</span><span>|</span>
      <span>2093</span>
    </footer>
  </section>

  <section class="card card-back" aria-label="Business card back">
    <div class="back-photo" role="img" aria-label="Blue-tinted photograph of engineering plans, hard hat, rulers and a tape measure"></div>
    <div class="wordmark">
      <span class="wordmark-mark" aria-hidden="true"></span>
      <span class="wordmark-name">Pelloway Civil Engineering</span>
      <span class="wordmark-sub">Services</span>
    </div>
  </section>
</main>
</body>
</html>
```